Northfield Builders Guild Business card

We are looking for a new business card design with photo included.
Our business is a nonprofit construction contractor membership organization. We offer business education, assist with business setup and licensing, provide safety training, and provide a member directory.
URL: www.brickwayguildnetwork.org
Color code:
CMYK: 0 cyan, 42 magenta, 100 yellow, 0 black for Print.
Hexidecimal: #FF9900
RGB: R 255; G 153; B 0

```html
<!DOCTYPE html>
<html lang="en">
<head>
<meta charset="utf-8">
<title>Northfield Builders Guild – Business Card</title>
<link rel="stylesheet" href="https://fonts.googleapis.com/css2?family=Oswald:wght@500&family=Jost:wght@400;700&display=swap">
<style>
  :root {
    --backdrop: #8a8a8a;
    --paper: #ffffff;
    --charcoal: #333132;
    --card-dark: #353435;
    --emboss: #4b4a4b;
    --orange: #ff9900;
    --ink: #3a3a3a;
  }
  * { margin: 0; padding: 0; box-sizing: border-box; }
  html, body { width: 1200px; height: 1200px; overflow: hidden; }
  body {
    background: var(--backdrop);
    position: relative;
    font-family: "Jost", sans-serif;
  }
  .card {
    position: absolute;
    left: 262px;
    width: 686px;
    height: 392px;
  }
  .card-front { top: 165px; background: var(--paper); }
  .card-back { top: 653px; background: var(--card-dark); }

  .brand {
    position: absolute;
    display: flex;
    align-items: center;
    gap: 10px;
    font-family: "Jost", sans-serif;
    font-weight: 700;
    letter-spacing: 0.5px;
    white-space: nowrap;
  }
  .brand-square {
    width: 16px; height: 16px;
    background: var(--orange);
  }
  .card-front .brand {
    left: 221px; top: 204px;
    transform: translate(-50%, -50%);
    font-size: 25px;
    color: var(--charcoal);
  }
  .card-back .brand {
    left: 50%; top: 50%;
    transform: translate(-50%, -50%);
    font-size: 36px;
    color: var(--emboss);
  }

  .contact {
    position: absolute;
    left: 396px;
    top: 76px;
    color: var(--ink);
  }
  .contact-name {
    font-family: "Oswald", sans-serif;
    font-weight: 500;
    font-size: 28px;
    line-height: 1.2;
    color: var(--charcoal);
    letter-spacing: 0.3px;
  }
  .contact-title {
    font-size: 16px;
    color: var(--orange);
    line-height: 1.2;
  }
  .contact-rule {
    width: 79px;
    height: 1px;
    background: var(--charcoal);
    margin: 12px 0 23px;
  }
  .contact-block {
    font-size: 16px;
    line-height: 19.5px;
  }
  .contact-block + .contact-block { margin-top: 12px; }
  .contact-web { margin-top: 19px; font-size: 16px; }

  .edge-band {
    position: absolute;
    bottom: 0;
    height: 10px;
  }
  .edge-band-dark { left: 0; width: 380px; background: var(--charcoal); }
  .edge-band-accent { left: 382px; right: 0; background: var(--orange); }
</style>
</head>
<body>
  <section class="card card-front">
    <div class="brand"><span class="brand-square"></span>Northfield Builders Guild</div>
    <div class="contact">
      <div class="contact-name">DANA WHITCOMB</div>
      <div class="contact-title">President</div>
      <div class="contact-rule"></div>
      <div class="contact-block">
        4820 NW Alder Ridge Rd.,<br>
        Suite #210<br>
        Corvallis, OR 97330
      </div>
      <div class="contact-block">
        Tel . (541) 555-0183<br>
        Cell . 541.555.0147<br>
        Email . hello@brickwayguild.org
      </div>
      <div class="contact-web">brickwayguildnetwork.org</div>
    </div>
    <div class="edge-band edge-band-dark"></div>
    <div class="edge-band edge-band-accent"></div>
  </section>

  <section class="card card-back">
    <div class="brand">Northfield Builders Guild</div>
  </section>
</body>
</html>
```